Lien Post Card - (5.5 x 8.5)

FRONT OF POSTCARD
Is a Property Lien Putting Your Home at Risk?
HOA Liens • Tax Liens • Municipal Charges • Other Property-Related Liens
You may have options to resolve outstanding liens and protect your home.
A Refinance or Home Equity Line of Credit (HELOC) may help you:
✔ Pay off qualifying liens
✔ Consolidate debt into one manageable payment
✔ Access your home's equity
✔ Improve your financial flexibility
✔ Avoid additional penalties, fees, or collection actions
Don't wait until the situation becomes more difficult.
Call today for a confidential review of your options.
Bluegate Lending Partners, Inc.
(800) 647-2915 x 42
www.bluegatelendco.com
NMLS #381640
BACK OF POSTCARD
Your Home Equity Could Be the Solution
If you have received notices regarding:
• Delinquent Property Taxes
• HOA or Condo Association Assessments
• Municipal Utility Liens
• Special Assessments
• Other Property-Related Obligations
You may qualify for financing options designed to help satisfy those obligations and bring your property current.
Our experienced mortgage professionals can review your situation and discuss available programs, including:
• Cash-Out Refinancing
• Home Equity Lines of Credit (HELOCs)
• Home Equity Loans
• Debt Consolidation Solutions
Free Consultation • No Obligation
Contact Marcus Delaney today at (800) 647-2915 x42 or mdelaney@bluegatelendco.com (NMLS #57308)

```html
<!DOCTYPE html>
<html lang="en">
<head>
<meta charset="utf-8">
<title>Property Lien Postcard – Bluegate Lending Partners</title>
<link href="https://fonts.googleapis.com/css2?family=Anton&family=Montserrat:ital,wght@0,500;0,600;0,700;0,800;1,500;1,700&display=swap" rel="stylesheet">
<style>
  :root{
    --navy:#0f2470;
    --royal:#1f3fae;
    --gold:#e9ac3a;
    --gold-deep:#d99a22;
    --ink:#141821;
    --white:#ffffff;
    --paper:#e9eaec;
    --stage:#8f8f8f;
    --rule:#b9bcc4;
  }
  *{box-sizing:border-box;margin:0;padding:0}
  html,body{width:1200px;height:2228px;overflow:hidden}
  body{background:var(--stage);font-family:"Montserrat",sans-serif;position:relative}
  .card{position:absolute;left:50px;width:1100px;height:712px;overflow:hidden;box-shadow:0 6px 14px rgba(0,0,0,.35)}
  .card--front{top:372px;background:#3a2a1c}
  .card--back{top:1144px;background:var(--white)}
  .abs{position:absolute}

  /* FRONT */
  .scene-photo{left:0;top:0;width:1100px;height:600px;
    background:linear-gradient(180deg,#5b5046 0%,#8a7354 30%,#c08a3e 52%,#3b2b1a 72%,#0d0b09 100%)}
  .portrait-photo{left:720px;top:20px;width:380px;height:580px;
    background:linear-gradient(160deg,#2b2c33 0%,#1a1b22 60%,#0f1016 100%);border-radius:180px 180px 0 0}
  .headline-lead{left:30px;top:18px;font-family:"Anton",sans-serif;color:var(--white);font-size:38px;line-height:1}
  .headline-main{left:30px;top:54px;font-family:"Anton",sans-serif;color:var(--white);font-size:104px;line-height:1;letter-spacing:1px}
  .headline-sub{left:32px;top:150px;font-family:"Anton",sans-serif;color:var(--gold);font-size:40px;line-height:1}
  .lien-types{left:34px;top:190px;height:32px;padding:0 16px;background:var(--royal);color:var(--white);
    font-size:16px;font-weight:500;display:flex;align-items:center;gap:7px;white-space:nowrap}
  .dot{width:8px;height:8px;border-radius:50%;background:var(--gold);display:inline-block}
  .front-intro{left:34px;top:237px;color:var(--white);font-size:18px;font-weight:500}
  .front-lead{left:34px;top:289px;color:var(--gold);font-size:17px;font-weight:800}
  .checklist{list-style:none}
  .checklist li{display:flex;align-items:center;gap:10px;height:27px;font-weight:700;font-size:17px}
  .checklist svg{flex:none}
  .front-list{left:34px;top:318px;color:var(--white)}
  .urgency-band{left:0;top:496px;width:1100px;height:46px;background:var(--gold)}
  .urgency-text{left:34px;top:501px;display:flex;align-items:center;gap:12px;color:var(--ink);font-size:16.5px;font-weight:700;line-height:1.15}
  .urgency-text em{font-style:italic}
  .inset-photo{top:459px;width:210px;height:114px;border:3px solid var(--gold);border-radius:8px}
  .inset-photo--a{left:624px;background:linear-gradient(135deg,#c9cbd0,#6f7786 60%,#3c4250)}
  .inset-photo--b{left:844px;background:linear-gradient(135deg,#dcdad4,#4c6a8a 55%,#2d3b4e)}
  .black-strip{left:0;top:542px;width:1100px;height:58px;background:#050505}
  .footer-band{left:0;top:600px;width:1100px;height:112px;background:var(--navy)}
  .brand{color:var(--white);font-weight:800;font-size:24px;line-height:1.15;display:flex;align-items:center;gap:12px}
  .brand-mark{width:18px;height:18px;border-radius:50%;background:var(--gold);flex:none}
  .front-brand{left:34px;top:620px;width:280px}
  .divider{width:2px;background:rgba(255,255,255,.55)}
  .front-divider{left:334px;top:610px;height:92px}
  .contact-phone{color:var(--white);font-weight:700;font-size:46px;line-height:1}
  .contact-web{color:var(--white);font-weight:700;font-size:30px;line-height:1;white-space:nowrap}
  .contact-web .sep{font-weight:500;margin:0 14px;opacity:.8}
  .front-phone{left:383px;top:614px}
  .front-web{left:385px;top:666px}

  /* BACK */
  .message-panel{left:0;top:0;width:617px;height:531px;background:linear-gradient(180deg,#f3f3f4 0%,var(--paper) 100%)}
  .skyline-fade{left:0;top:150px;width:617px;height:300px;background:linear-gradient(180deg,rgba(190,192,198,0) 0%,rgba(190,192,198,.45) 55%,rgba(190,192,198,0) 100%)}
  .back-title{left:34px;top:30px;font-family:"Anton",sans-serif;font-size:40px;line-height:1.05}
  .back-title .gold{color:var(--gold)}
  .back-title .navy{color:var(--navy)}
  .back-lead{left:36px;top:122px;color:var(--gold);font-size:17px;font-weight:800}
  .back-list{left:34px;top:148px;color:var(--ink)}
  .back-list li{height:29px}
  .back-note{left:34px;top:317px;width:560px;color:var(--ink);font-size:17px;font-style:italic;font-weight:500;line-height:1.12}
  .back-body{left:34px;top:374px;width:560px;color:var(--ink);font-size:17px;font-weight:500;line-height:1.25}
  .programs{left:30px;top:422px;width:580px;display:grid;grid-template-columns:318px 262px;row-gap:8px}
  .program{display:flex;align-items:center;gap:14px;font-size:17px;font-weight:600;color:var(--ink);line-height:1.15}
  .program svg{flex:none}
  .address-divider{left:616px;top:28px;width:2px;height:503px;background:var(--navy)}
  .back-brand{left:660px;top:62px;width:220px;color:var(--navy);font-size:18px}
  .stamp-box{left:947px;top:27px;width:109px;height:108px;border:1.5px solid #a6a8ad;background:#eceded}
  .address-line{left:670px;width:386px;height:1.5px;background:var(--rule)}
  .consult-band{left:0;top:531px;width:1100px;height:45px;background:var(--gold)}
  .consult-text{left:155px;top:539px;color:var(--navy);font-size:25px;font-weight:800;white-space:nowrap}
  .back-footer{left:0;top:576px;width:1100px;height:136px;background:var(--navy)}
  .agent-photo{left:22px;top:552px;width:120px;height:120px;border-radius:50%;border:4px solid var(--white);
    background:linear-gradient(180deg,#b9bcc2 0%,#3a3c44 60%,#15161b 100%)}
  .agent-block{left:155px;top:596px;color:var(--white);line-height:1}
  .agent-block .small{font-size:13px;font-weight:600;letter-spacing:.3px}
  .agent-block .name{font-size:26px;font-weight:800;margin:3px 0;line-height:.98}
  .back-divider{left:334px;top:596px;height:98px}
  .back-phone{left:383px;top:604px}
  .back-web{left:385px;top:656px}
</style>
</head>
<body>

<!-- FRONT -->
<section class="card card--front">
  <div class="abs scene-photo" role="img" aria-label="City skyline silhouetted against a golden sunset sky"></div>
  <div class="abs portrait-photo" role="img" aria-label="Portrait of the loan officer in a dark hat, glasses and black coat"></div>

  <div class="abs headline-lead">IS A</div>
  <h1 class="abs headline-main">PROPERTY LIEN</h1>
  <div class="abs headline-sub">PUTTING YOUR HOME AT RISK?</div>

  <div class="abs lien-types">HOA Liens <span class="dot"></span> Tax Liens <span class="dot"></span> Municipal Charges <span class="dot"></span> Other Property-Related Liens</div>

  <p class="abs front-intro">You may have options to resolve outstanding liens and protect your home.</p>
  <p class="abs front-lead">A Refinance or Home Equity Line of Credit (HELOC) may help you:</p>

  <ul class="abs checklist front-list">
    <li><svg width="14" height="14" viewBox="0 0 14 14"><circle cx="7" cy="7" r="7" fill="#e9ac3a"/><path d="M3.8 7.2l2.1 2.1 4.3-4.4" stroke="#141821" stroke-width="1.8" fill="none"/></svg>Pay off qualifying liens</li>
    <li><svg width="14" height="14" viewBox="0 0 14 14"><circle cx="7" cy="7" r="7" fill="#e9ac3a"/><path d="M3.8 7.2l2.1 2.1 4.3-4.4" stroke="#141821" stroke-width="1.8" fill="none"/></svg>Consolidate debt into one manageable payment</li>
    <li><svg width="14" height="14" viewBox="0 0 14 14"><circle cx="7" cy="7" r="7" fill="#e9ac3a"/><path d="M3.8 7.2l2.1 2.1 4.3-4.4" stroke="#141821" stroke-width="1.8" fill="none"/></svg>Access your home's equity</li>
    <li><svg width="14" height="14" viewBox="0 0 14 14"><circle cx="7" cy="7" r="7" fill="#e9ac3a"/><path d="M3.8 7.2l2.1 2.1 4.3-4.4" stroke="#141821" stroke-width="1.8" fill="none"/></svg>Improve your financial flexibility</li>
    <li><svg width="14" height="14" viewBox="0 0 14 14"><circle cx="7" cy="7" r="7" fill="#e9ac3a"/><path d="M3.8 7.2l2.1 2.1 4.3-4.4" stroke="#141821" stroke-width="1.8" fill="none"/></svg>Avoid additional penalties, fees, or collection actions</li>
  </ul>

  <div class="abs urgency-band"></div>
  <div class="abs urgency-text">
    <svg width="22" height="22" viewBox="0 0 22 22"><circle cx="11" cy="11" r="10" fill="none" stroke="#141821" stroke-width="2"/><path d="M7.2 6.2c.6-.6 1.4-.5 1.8.1l1 1.6c.3.5.2 1.1-.2 1.5l-.6.5c.6 1.3 1.6 2.3 2.9 2.9l.5-.6c.4-.4 1-.5 1.5-.2l1.6 1c.6.4.7 1.2.1 1.8l-.8.8c-.7.7-1.8.8-2.7.3-2.3-1.2-4.1-3-5.3-5.3-.5-.9-.4-2 .3-2.7z" fill="#141821"/></svg>
    <div>Don't wait until the situation becomes more difficult.<br><em>Call today</em> for a confidential review of your options.</div>
  </div>

  <div class="abs inset-photo inset-photo--a" role="img" aria-label="Worried couple reviewing bills on a laptop"></div>
  <div class="abs inset-photo inset-photo--b" role="img" aria-label="Stressed man holding his head over paperwork"></div>

  <div class="abs black-strip"></div>
  <div class="abs footer-band"></div>
  <div class="abs brand front-brand"><span class="brand-mark"></span><span>Bluegate Lending Partners, Inc.</span></div>
  <div class="abs divider front-divider"></div>
  <div class="abs contact-phone front-phone">(800) 647-2915 x 42</div>
  <div class="abs contact-web front-web">www.bluegatelendco.com<span class="sep">|</span>NMLS #381640</div>
</section>

<!-- BACK -->
<section class="card card--back">
  <div class="abs message-panel"></div>
  <div class="abs skyline-fade" role="img" aria-label="Faint city skyline in light grey"></div>

  <h2 class="abs back-title"><span class="gold">YOUR HOME EQUITY</span><br><span class="navy">COULD BE THE SOLUTION</span></h2>
  <p class="abs back-lead">If you have received notices regarding:</p>

  <ul class="abs checklist back-list">
    <li><svg width="13" height="13" viewBox="0 0 14 14"><circle cx="7" cy="7" r="7" fill="#e9ac3a"/><path d="M3.8 7.2l2.1 2.1 4.3-4.4" stroke="#fff" stroke-width="1.8" fill="none"/></svg>Pay off qualifying liens</li>
    <li><svg width="13" height="13" viewBox="0 0 14 14"><circle cx="7" cy="7" r="7" fill="#e9ac3a"/><path d="M3.8 7.2l2.1 2.1 4.3-4.4" stroke="#fff" stroke-width="1.8" fill="none"/></svg>Consolidate debt into one manageable payment</li>
    <li><svg width="13" height="13" viewBox="0 0 14 14"><circle cx="7" cy="7" r="7" fill="#e9ac3a"/><path d="M3.8 7.2l2.1 2.1 4.3-4.4" stroke="#fff" stroke-width="1.8" fill="none"/></svg>Access your home's equity</li>
    <li><svg width="13" height="13" viewBox="0 0 14 14"><circle cx="7" cy="7" r="7" fill="#e9ac3a"/><path d="M3.8 7.2l2.1 2.1 4.3-4.4" stroke="#fff" stroke-width="1.8" fill="none"/></svg>Improve your financial flexibility</li>
    <li><svg width="13" height="13" viewBox="0 0 14 14"><circle cx="7" cy="7" r="7" fill="#e9ac3a"/><path d="M3.8 7.2l2.1 2.1 4.3-4.4" stroke="#fff" stroke-width="1.8" fill="none"/></svg>Avoid additional penalties, fees, or collection actions</li>
  </ul>

  <p class="abs back-note">You may qualify for financing options designed to help satisfy those obligations and bring your property current.</p>
  <p class="abs back-body">Our experienced mortgage professionals can review your situation and discuss available programs, including:</p>

  <div class="abs programs">
    <div class="program"><svg width="36" height="36" viewBox="0 0 36 36"><circle cx="18" cy="18" r="16" fill="#f6e3bd" stroke="#d99a22" stroke-width="2"/><path d="M10 19l8-7 8 7M13 17v8h10v-8" stroke="#d99a22" stroke-width="2" fill="none"/></svg>Cash-Out Refinancing</div>
    <div class="program"><svg width="36" height="36" viewBox="0 0 36 36"><circle cx="18" cy="18" r="16" fill="#f6e3bd" stroke="#d99a22" stroke-width="2"/><path d="M10 19l8-7 8 7M13 17v8h10v-8" stroke="#d99a22" stroke-width="2" fill="none"/></svg>Home Equity Loans</div>
    <div class="program"><svg width="36" height="36" viewBox="0 0 36 36"><circle cx="18" cy="18" r="16" fill="#f6e3bd" stroke="#d99a22" stroke-width="2"/><path d="M10 19l8-7 8 7M13 17v8h10v-8" stroke="#d99a22" stroke-width="2" fill="none"/></svg>Home Equity Lines of<br>Credit (HELOCs)</div>
    <div class="program"><svg width="36" height="36" viewBox="0 0 36 36"><circle cx="18" cy="18" r="16" fill="#f6e3bd" stroke="#d99a22" stroke-width="2"/><circle cx="18" cy="18" r="6" stroke="#d99a22" stroke-width="2" fill="none"/></svg>Debt Consolidation<br>Solutions</div>
  </div>

  <div class="abs address-divider"></div>
  <div class="abs brand back-brand"><span class="brand-mark"></span><span>Bluegate Lending Partners, Inc.</span></div>
  <div class="abs stamp-box"></div>
  <div class="abs address-line" style="top:199px"></div>
  <div class="abs address-line" style="top:249px"></div>
  <div class="abs address-line" style="top:303px"></div>

  <div class="abs consult-band"></div>
  <div class="abs consult-text">FREE CONSULTATION • NO OBLIGATION</div>
  <div class="abs back-footer"></div>
  <div class="abs agent-photo" role="img" aria-label="Round portrait of loan officer Marcus Delaney"></div>
  <div class="abs agent-block">
    <div class="small">CONTACT</div>
    <div class="name">MARCUS<br>DELANEY</div>
    <div class="small">TODAY AT</div>
  </div>
  <div class="abs divider back-divider"></div>
  <div class="abs contact-phone back-phone">(800) 647-2915 x 42</div>
  <div class="abs contact-web back-web">www.bluegatelendco.com<span class="sep">|</span>NMLS #381640</div>
</section>

</body>
</html>
```